Vordaline - Fitness Coach. Needs a Business Card Design that I can also use for other advertising

Established 2012, I have finished the KTRB National Certificate in Fitness & Personal Training. Harlow Cross First Aid Certificate. I have the Auckland 800m track records for MW45. I also came 1st at the 2012 Pellamar Games in 800 & 1500m. I am passionate about health & fitness and would like to help people reach their health & fitness goals. I also take health & fitness weekends. Main interests - Running, Weight Training, Yoga & Aqua Jogging. I like strength/power, but am femine.

Target Market(s)

Male or Female 18 and over that wants to improve their health & fitness

Industry/Entity Type

Advertising

Requirements
Must have
• my name: Rosalind K Tarbury contact details: ros@quillsend.co.nz mobile - 021 583917 URL name: facebook.com/rosalindKtarbury - VordaLine
Photo of Me

```html
<!DOCTYPE html>
<html lang="en">
<head>
<meta charset="utf-8">
<title>Vordaline – Fitness Coach Business Card</title>
<link rel="stylesheet" href="https://fonts.googleapis.com/css2?family=Roboto+Condensed:wght@300;400&family=Roboto:wght@300;400&display=swap">
<style>
  :root{
    --page:#ececec;
    --lime:#b6f200;
    --lime-soft:#9fd81a;
    --green:#2fc400;
    --green-deep:#009a00;
    --green-dark:#003d00;
    --ink:#0b0b0b;
    --white:#ffffff;
    --grey-text:#9a9a9a;
    --icon-green:#3fbf2a;
    --photo-leaf:#3f6a1c;
    --photo-shade:#1d3510;
  }
  *{margin:0;padding:0;box-sizing:border-box}
  html,body{width:1200px;height:848px;overflow:hidden;background:var(--page)}
  .canvas{position:relative;width:1200px;height:848px}

  .card{position:absolute;top:285px;width:514px;height:309px;overflow:hidden}

  /* front */
  .card-front{left:69px;background:linear-gradient(90deg,var(--green) 0%,var(--lime-soft) 30%,var(--lime) 60%,var(--green) 100%);border-radius:0 22px 22px 0}
  .front-tint{position:absolute;inset:0;background:linear-gradient(180deg,rgba(0,80,0,.15),rgba(255,255,120,.12) 40%,rgba(0,60,0,.25))}
  .front-block{position:absolute;left:0;width:83px;background:rgba(0,120,0,.35)}
  .front-block.b1{top:31px;height:18px}
  .front-block.b2{top:100px;height:34px}
  .front-photo{position:absolute;left:83px;top:0;width:204px;height:309px;background:radial-gradient(ellipse at 45% 45%,var(--photo-leaf),var(--photo-shade))}
  .front-edge{position:absolute;left:460px;top:0;width:54px;height:309px;background:linear-gradient(180deg,var(--green-dark),#004f00 50%,var(--green-dark));border-radius:0 22px 22px 0}
  .front-edge-band{position:absolute;left:460px;top:32px;width:54px;height:70px;background:var(--green-deep)}
  .stripe{position:absolute;left:0;width:460px;background:linear-gradient(90deg,var(--lime),var(--green) 55%,var(--green-deep))}
  .stripe.s1{top:187px;height:5px}
  .stripe.s2{top:198px;height:4px;background:var(--green-dark)}
  .stripe.s3{top:207px;height:26px;width:514px}
  .stripe.s4{top:236px;height:3px;background:var(--lime)}
  .stripe.s5{top:242px;height:19px;width:514px}
  .stripe.s6{top:266px;height:14px;background:linear-gradient(90deg,var(--green-dark),var(--green) 60%,var(--green-dark))}
  .brand{position:absolute;right:54px;top:200px;font-family:"Roboto Condensed",sans-serif;font-weight:400;font-size:27px;color:var(--white);letter-spacing:-.3px}
  .tagline{position:absolute;right:54px;top:240px;font-family:"Roboto",sans-serif;font-weight:300;font-size:13.5px;color:var(--white);white-space:nowrap}

  /* back */
  .card-back{left:616px;background:var(--ink)}
  .back-photo{position:absolute;inset:0;background:radial-gradient(ellipse at 40% 40%,#3a3a3a,#1c1c1c 55%,#0f0f0f)}
  .back-row{position:absolute;left:0;width:514px;height:18px;background:rgba(0,0,0,.55)}
  .back-row.r1{top:24px}.back-row.r2{top:206px}.back-row.r3{top:250px}
  .bar{position:absolute;height:6px}
  .bar.g1{top:94px;left:0;width:514px;height:5px;background:linear-gradient(90deg,var(--lime),var(--green))}
  .bar.g2{top:102px;left:0;width:514px;height:14px;background:linear-gradient(90deg,var(--lime),var(--green) 50%,var(--green-deep))}
  .bar.k1{top:108px;left:136px;width:378px;height:5px;background:var(--ink)}
  .bar.g3{top:120px;left:0;width:514px;height:5px;background:linear-gradient(90deg,var(--green),var(--green-deep))}
  .bar.g4{top:130px;left:0;width:514px;height:36px;background:linear-gradient(90deg,var(--lime),var(--green) 55%,var(--green-deep))}
  .bar.k2{top:147px;left:295px;width:219px;height:6px;background:var(--ink)}
  .bar.g5{top:170px;left:0;width:514px;height:5px;background:var(--lime)}
  .bar.g6{top:180px;left:0;width:514px;height:5px;background:linear-gradient(90deg,var(--green),var(--green-deep))}
  .name{position:absolute;left:38px;top:131px;font-family:"Roboto Condensed",sans-serif;font-weight:400;font-size:30px;color:var(--white);letter-spacing:-.3px;white-space:nowrap}
  .role{position:absolute;left:38px;top:186px;font-family:"Roboto",sans-serif;font-weight:300;font-size:17px;color:var(--grey-text)}
  .contacts{position:absolute;left:227px;top:204px;list-style:none;font-family:"Roboto Condensed",sans-serif;font-weight:400;font-size:14px;color:var(--white)}
  .contacts li{display:flex;align-items:center;height:25.5px;white-space:nowrap}
  .icon{width:12px;height:12px;margin-right:4px;flex:none}
  .icon-square{background:var(--icon-green);border-radius:2px}
</style>
</head>
<body>
<main class="canvas">

  <section class="card card-front" aria-label="Business card front">
    <div class="front-tint"></div>
    <div class="front-block b1"></div>
    <div class="front-block b2"></div>
    <div class="front-photo" role="img" aria-label="Photo of the coach jumping in front of green foliage"></div>
    <div class="front-edge"></div>
    <div class="front-edge-band"></div>
    <div class="stripe s1"></div>
    <div class="stripe s2"></div>
    <div class="stripe s3"></div>
    <div class="stripe s4"></div>
    <div class="stripe s5"></div>
    <div class="stripe s6"></div>
    <p class="brand">VordaLine</p>
    <p class="tagline">meeting your health &amp; fitness goals</p>
  </section>

  <section class="card card-back" aria-label="Business card back">
    <div class="back-photo" role="img" aria-label="Faint dark photo of the coach in motion"></div>
    <div class="back-row r1"></div>
    <div class="back-row r2"></div>
    <div class="back-row r3"></div>
    <div class="bar g1"></div>
    <div class="bar g2"></div>
    <div class="bar k1"></div>
    <div class="bar g3"></div>
    <div class="bar g4"></div>
    <div class="bar k2"></div>
    <div class="bar g5"></div>
    <div class="bar g6"></div>
    <h1 class="name">Rosalind K. Tarbury</h1>
    <p class="role">Fitness Coach</p>
    <ul class="contacts">
      <li>
        <svg class="icon" viewBox="0 0 12 12" aria-hidden="true"><rect width="12" height="12" rx="2.5" fill="#3fbf2a"/><rect x="2.5" y="3.5" width="7" height="5" fill="#fff"/><path d="M2.5 3.5 6 6.5 9.5 3.5" fill="none" stroke="#3fbf2a" stroke-width=".8"/></svg>
        ros@quillsend.co.nz
      </li>
      <li>
        <svg class="icon" viewBox="0 0 12 12" aria-hidden="true"><rect width="12" height="12" rx="2.5" fill="#3fbf2a"/><rect x="4" y="2" width="4" height="8" rx=".8" fill="#fff"/></svg>
        021 583917
      </li>
      <li>
        <span class="icon icon-square" aria-hidden="true"></span>
        fitlink.co.nz/rosalindKtarbury-VordaLine
      </li>
    </ul>
  </section>

</main>
</body>
</html>
```